Business Card Design Project

I need a business card for a Management Consultancy. We work with organisational design and development and strategic change using facilitation, consulting and coaching.

Size of card is 90 x 55mm.

Logo is attached.

Wording is:

Maria Kestle
Director

tel 0491627358
email is: info@tallowpoint.com.au

Target Market(s)

Government departments and not for profit organisations mainly.

Industry/Entity Type

Business

Requirements
Must have
• White or colour background not black.

On one side of the card, either back or front please include the words:

Leading Strategic Change

Two sided business card

```html
<!DOCTYPE html>
<html lang="en">
<head>
<meta charset="utf-8">
<title>Tallow Point – Business Card</title>
<link rel="stylesheet" href="https://fonts.googleapis.com/css2?family=Open+Sans:wght@400;600&display=swap">
<style>
  :root {
    --navy: #2c4a6e;
    --navy-light: #4674a4;
    --green: #8bc141;
    --white: #ffffff;
    --page: #ffffff;
    --shadow: 0 6px 22px rgba(0, 0, 0, 0.32);
  }
  html, body {
    margin: 0;
    padding: 0;
    width: 1200px;
    height: 827px;
    overflow: hidden;
    background: var(--page);
    font-family: "Open Sans", Arial, sans-serif;
  }
  .canvas {
    position: relative;
    width: 1200px;
    height: 827px;
  }
  .card {
    position: absolute;
    width: 506px;
    height: 285px;
    box-shadow: var(--shadow);
    overflow: hidden;
  }
  .card-front { left: 62px; top: 288px; background: var(--white); }
  .card-back-light { left: 646px; top: 107px; background: var(--white); }
  .card-back-dark { left: 644px; top: 453px; background: var(--navy); }

  .front-graphics {
    position: absolute;
    inset: 0;
    width: 100%;
    height: 100%;
  }
  .company-name {
    position: absolute;
    left: 34px;
    top: 38px;
    margin: 0;
    font-size: 22px;
    font-weight: 400;
    color: var(--navy);
  }
  .person-name {
    position: absolute;
    left: 51px;
    top: 144px;
    margin: 0;
    font-size: 25px;
    font-weight: 400;
    color: var(--white);
  }
  .contact {
    position: absolute;
    left: 29px;
    top: 237px;
    margin: 0;
    font-size: 12px;
    line-height: 16px;
    display: grid;
    grid-template-columns: 44px auto;
  }
  .contact dt { color: var(--navy); }
  .contact dd { margin: 0; color: var(--white); }

  .tagline {
    position: absolute;
    inset: 0;
    display: flex;
    align-items: center;
    justify-content: center;
    margin: 0;
    font-size: 22px;
    font-weight: 400;
    color: var(--green);
  }
</style>
</head>
<body>
<main class="canvas">

  <section class="card card-front" aria-label="Card front">
    <svg class="front-graphics" viewBox="0 0 492 277" preserveAspectRatio="none" aria-hidden="true">
      <defs>
        <linearGradient id="bandGradient" gradientUnits="userSpaceOnUse" x1="0" y1="0" x2="492" y2="0">
          <stop offset="0" stop-color="#2c4a6e"/>
          <stop offset="0.5" stop-color="#4674a4"/>
          <stop offset="1" stop-color="#2c4a6e"/>
        </linearGradient>
      </defs>
      <rect class="name-band" x="0" y="108" width="492" height="100" fill="url(#bandGradient)"/>
      <polygon class="diagonal-stripe" points="440,0 492,0 346,277 294,277" fill="url(#bandGradient)"/>
      <polygon class="corner-accent" points="492,20 492,100 449,100" fill="#8bc141"/>
      <polygon class="footer-left" points="0,217 317,217 285,277 0,277" fill="#8bc141"/>
      <polygon class="footer-right" points="388,217 492,217 492,277 356,277" fill="#8bc141"/>
    </svg>

    <p class="company-name">Tallow Point</p>

    <h1 class="person-name">Maria Kestle</h1>

    <dl class="contact">
      <dt>E-mail:</dt><dd>info@tallowpoint.com.au</dd>
      <dt>Phone:</dt><dd>0491627358</dd>
    </dl>
  </section>

  <section class="card card-back-light" aria-label="Card back, light version">
    <p class="tagline">Leading Strategic Change</p>
  </section>

  <section class="card card-back-dark" aria-label="Card back, dark version">
    <p class="tagline">Leading Strategic Change</p>
  </section>

</main>
</body>
</html>
```